Brightvale Marketing Banner for emails to customers

Hi Marketing Team The information is to be a nice banner say half page on Marketing our Services to prospective customers, this is embedded into an email so something nice with the content that I will provide. Based on a nice background to highlight our service portfolio aligned to our website
www.brightvale-example.com.au

```html
<!DOCTYPE html>
<html lang="en">
<head>
<meta charset="utf-8">
<title>Brightvale – Cleaning Experts</title>
<link rel="stylesheet" href="https://fonts.googleapis.com/css2?family=Montserrat:wght@400;500;600;700&display=swap">
<style>
  :root {
    --orange: #ff5208;
    --navy: #0b3a6e;
    --ink: #333333;
    --text: #1c1c1c;
    --pale-blue: #e8f0fa;
    --white: #ffffff;
    --wood: #8a4a22;
    --cabinet: #e9e9e6;
  }
  html, body {
    margin: 0;
    padding: 0;
    width: 1200px;
    height: 960px;
    overflow: hidden;
    background: var(--white);
  }
  .banner {
    position: relative;
    width: 1200px;
    height: 960px;
    overflow: hidden;
    background: var(--white);
    font-family: "Montserrat", Arial, sans-serif;
    color: var(--text);
  }
  .backdrop {
    position: absolute;
    inset: 0;
  }
  .brand {
    position: absolute;
    left: 58px;
    top: 60px;
    display: flex;
    align-items: center;
    gap: 12px;
  }
  .brand-dot {
    width: 38px;
    height: 38px;
    border-radius: 50%;
    background: var(--navy);
  }
  .brand-name {
    font-size: 40px;
    font-weight: 500;
    color: var(--orange);
    letter-spacing: -0.5px;
  }
  .headline {
    position: absolute;
    left: 50px;
    top: 208px;
    margin: 0;
    font-size: 113px;
    font-weight: 700;
    line-height: 98px;
    color: var(--ink);
    letter-spacing: 1px;
  }
  .tenure {
    position: absolute;
    left: 56px;
    top: 432px;
    margin: 0;
    font-size: 32px;
    font-weight: 400;
    color: var(--ink);
    letter-spacing: 0.5px;
  }
  .tenure strong { color: var(--orange); font-weight: 700; }
  .tenure-rule {
    position: absolute;
    left: 56px;
    top: 491px;
    width: 172px;
    height: 4px;
    background: var(--orange);
  }
  .services-title {
    position: absolute;
    left: 57px;
    top: 571px;
    margin: 0;
    font-size: 30px;
    font-weight: 700;
    color: var(--navy);
  }
  .services-title span { color: var(--orange); }
  .services-list {
    position: absolute;
    left: 56px;
    top: 620px;
    margin: 0;
    padding: 0;
    list-style: none;
    font-size: 20.5px;
    font-weight: 500;
    line-height: 26.5px;
    color: #2a2a2a;
    letter-spacing: 0.3px;
  }
  .services-list li {
    display: flex;
    align-items: center;
    gap: 6px;
  }
  .services-list svg { flex: none; }
  .reputation {
    position: absolute;
    left: 58px;
    top: 774px;
    margin: 0;
    font-size: 25px;
    font-weight: 500;
    line-height: 30px;
    color: var(--text);
  }
  .reputation strong { font-weight: 700; }
  .contact-card {
    position: absolute;
    left: 620px;
    top: 510px;
    width: 492px;
    text-align: center;
    color: var(--white);
  }
  .contact-title {
    margin: 60px 0 0;
    font-size: 30px;
    font-weight: 600;
    letter-spacing: 1px;
  }
  .contact-blurb {
    margin: 12px auto 0;
    width: 400px;
    font-size: 24px;
    font-weight: 400;
    line-height: 29px;
  }
  .contact-rule {
    width: 186px;
    height: 1px;
    margin: 30px auto 0;
    background: rgba(255,255,255,0.45);
  }
  .contact-phone {
    margin: 22px 0 0;
    font-size: 48px;
    font-weight: 600;
    letter-spacing: 1px;
    line-height: 56px;
  }
  .contact-links {
    margin: 6px 0 0;
    font-size: 18.5px;
    font-weight: 600;
    line-height: 24px;
  }
</style>
</head>
<body>
<main class="banner">
  <svg class="backdrop" width="1200" height="960" viewBox="0 0 1200 960" aria-hidden="false">
    <defs>
      <linearGradient id="kitchen-tones" x1="0" y1="0" x2="0" y2="1">
        <stop offset="0" stop-color="#eeeeec"/>
        <stop offset="0.38" stop-color="var(--cabinet)"/>
        <stop offset="0.5" stop-color="#b8793f"/>
        <stop offset="1" stop-color="var(--wood)"/>
      </linearGradient>
    </defs>
    <circle class="pale-arc" cx="80" cy="1000" r="432" fill="var(--pale-blue)"/>
    <circle class="kitchen-photo" cx="960" cy="304" r="512" fill="url(#kitchen-tones)" role="img" aria-label="Photo of a clean white kitchen with shaker cabinets, a gas range and polished timber floor"/>
    <circle class="orange-arc" cx="528" cy="40" r="184" fill="var(--orange)"/>
    <circle class="contact-disc" cx="866" cy="736" r="246" fill="var(--navy)"/>
  </svg>

  <div class="brand">
    <span class="brand-dot"></span>
    <span class="brand-name">Brightvale</span>
  </div>

  <h1 class="headline">CLEANING<br>EXPERTS</h1>
  <p class="tenure">IN BUSINESS <strong>FOR 15 YEARS</strong></p>
  <div class="tenure-rule"></div>

  <h2 class="services-title">PORTFOLIO <span>OF SERVICES</span></h2>
  <ul class="services-list">
    <li><svg width="16" height="16" viewBox="0 0 16 16"><circle cx="8" cy="8" r="8" fill="var(--orange)"/><path d="M4.5 8.2l2.3 2.3 4.7-4.9" fill="none" stroke="#fff" stroke-width="1.8" stroke-linecap="round" stroke-linejoin="round"/></svg>Equipment Sundae Machine Cleaning Service</li>
    <li><svg width="16" height="16" viewBox="0 0 16 16"><circle cx="8" cy="8" r="8" fill="var(--orange)"/><path d="M4.5 8.2l2.3 2.3 4.7-4.9" fill="none" stroke="#fff" stroke-width="1.8" stroke-linecap="round" stroke-linejoin="round"/></svg>Detailed Kitchen Cleaning and Vat Boil Outs</li>
    <li><svg width="16" height="16" viewBox="0 0 16 16"><circle cx="8" cy="8" r="8" fill="var(--orange)"/><path d="M4.5 8.2l2.3 2.3 4.7-4.9" fill="none" stroke="#fff" stroke-width="1.8" stroke-linecap="round" stroke-linejoin="round"/></svg>Gurney High Pressure and Playground Cleaning</li>
    <li><svg width="16" height="16" viewBox="0 0 16 16"><circle cx="8" cy="8" r="8" fill="var(--orange)"/><path d="M4.5 8.2l2.3 2.3 4.7-4.9" fill="none" stroke="#fff" stroke-width="1.8" stroke-linecap="round" stroke-linejoin="round"/></svg>General Facility Maintenance</li>
  </ul>

  <p class="reputation">Brightvale is long known for <strong>a steady<br>and strong reputation</strong></p>

  <section class="contact-card">
    <h2 class="contact-title">SPECIALIZED</h2>
    <p class="contact-blurb">Our Team Members have received ongoing refresher training to keep skills refreshed and Market aligned</p>
    <div class="contact-rule"></div>
    <p class="contact-phone">1300 555 014</p>
    <p class="contact-links">SERVICE@BRIGHTVALE-EXAMPLE.COM.AU<br>WWW.BRIGHTVALE-EXAMPLE.COM.AU</p>
  </section>
</main>
</body>
</html>
```